RM Cargoline businesscard project

RM Cargoline Ltd is a freshly founded small (3 employees), young (average age is 30 years) company, living from the road transportation market without own tools.
We would like to have an impressive, new-line, cool busines card for a freshly founded forwarding company on an overcrowded market which raises attention and makes the potential partners eager to work with us.

Target Market(s)

The main profile of the company is logistic/forwarding on road.

Industry/Entity Type

Freight Forwarding

Contact Information for Business Card

Name: Berki Zsófia
Title: general manager
mobile nr: +36-70/482-5193
fax nr: +36-1/534-9061
e-mail: zsofia.berki@rmcargoline.example
info@rmcargoline.example
website address: http://www.rmcargoline.example
and if possible maybe some funny or helpful info on the back

Requirements
Must have
• contact details above
Nice to have
• some really nice and catching back-side (info, graphics, useful tool info... anything)
Should not have
• trucks, road, ship, airplane on it...

```html
<!DOCTYPE html>
<html lang="en">
<head>
<meta charset="utf-8">
<title>RM Cargoline – Business Card</title>
<link href="https://fonts.googleapis.com/css2?family=Oswald:wght@500&family=Montserrat:wght@500;700&display=swap" rel="stylesheet">
<style>
  :root {
    --backdrop: #a7cfcb;
    --card-dark: #29292b;
    --card-light: #eef1f3;
    --brand-blue: #4f86c6;
    --text-light: #ffffff;
    --text-dark: #232325;
  }
  * { box-sizing: border-box; margin: 0; padding: 0; }
  html, body {
    width: 1118px;
    height: 1200px;
    overflow: hidden;
    background: var(--backdrop);
  }
  .canvas { position: relative; width: 1118px; height: 1200px; }

  .card {
    position: absolute;
    overflow: hidden;
    box-shadow: 0 18px 30px rgba(0, 0, 0, 0.18);
  }

  /* Front side */
  .card-front {
    left: 232px; top: 110px;
    width: 648px; height: 402px;
    background: var(--card-dark);
  }
  .front-strip {
    position: absolute;
    height: 10px;
    background: var(--card-light);
  }
  .front-strip--top {
    top: 0; left: 0; width: 318px;
    clip-path: polygon(0 0, 100% 0, calc(100% - 14px) 100%, 0 100%);
  }
  .front-strip--bottom {
    bottom: 0; right: 0; width: 318px;
    clip-path: polygon(0 0, 100% 0, 100% 100%, 14px 100%);
  }
  .front-brand {
    position: absolute;
    left: 0; right: 0; top: 222px;
    display: flex; justify-content: center; align-items: center; gap: 14px;
  }
  .brand-square {
    width: 30px; height: 30px;
    background: var(--brand-blue);
  }
  .brand-name {
    font-family: "Oswald", sans-serif;
    font-weight: 500;
    letter-spacing: -0.5px;
    line-height: 1;
  }
  .front-brand .brand-name { font-size: 50px; color: var(--text-light); }
  .front-website {
    position: absolute;
    left: 0; right: 0; top: 318px;
    text-align: center;
    font-family: "Montserrat", sans-serif;
    font-weight: 500;
    font-size: 21px;
    color: var(--text-light);
  }

  /* Back side */
  .card-back {
    left: 231px; top: 659px;
    width: 651px; height: 407px;
    background: var(--card-light);
  }
  .back-shape { position: absolute; inset: 0; }
  .back-brand {
    position: absolute;
    left: 20px; width: 210px; top: 232px;
    display: flex; flex-direction: column; align-items: center; gap: 14px;
  }
  .back-brand .brand-square { width: 26px; height: 26px; }
  .back-brand .brand-name { font-size: 38px; color: var(--text-dark); }

  .holder {
    position: absolute;
    right: 21px; top: 118px;
    text-align: right;
    font-family: "Montserrat", sans-serif;
  }
  .holder-name {
    font-weight: 700;
    font-size: 29px;
    color: var(--text-light);
    line-height: 1.1;
    padding-bottom: 3px;
    border-bottom: 1.5px solid var(--text-light);
    padding-left: 4px;
  }
  .holder-title {
    margin-top: 3px;
    font-weight: 500;
    font-size: 12.5px;
    letter-spacing: 1.6px;
    color: var(--brand-blue);
    text-transform: uppercase;
  }

  .contact-list {
    position: absolute;
    right: 21px; top: 200px;
    list-style: none;
    font-family: "Montserrat", sans-serif;
    font-weight: 500;
    font-size: 16px;
    color: var(--text-light);
  }
  .contact-item {
    display: flex; justify-content: flex-end; align-items: center;
    gap: 10px;
    height: 26px;
  }
  .contact-icon { width: 16px; height: 16px; flex: none; }
</style>
</head>
<body>
<div class="canvas">

  <section class="card card-front" aria-label="Business card front">
    <div class="front-strip front-strip--top"></div>
    <div class="front-strip front-strip--bottom"></div>
    <div class="front-brand">
      <span class="brand-square"></span>
      <span class="brand-name">RM Cargoline</span>
    </div>
    <p class="front-website">www.rmcargoline.example</p>
  </section>

  <section class="card card-back" aria-label="Business card back">
    <svg class="back-shape" viewBox="0 0 651 407" width="651" height="407" aria-hidden="true">
      <path d="M520 0 C370 40 245 190 234 407 L651 407 L651 0 Z" fill="var(--brand-blue)"/>
      <path d="M616 0 C430 45 268 200 252 407 L651 407 L651 0 Z" fill="var(--card-dark)"/>
    </svg>

    <div class="back-brand">
      <span class="brand-square"></span>
      <span class="brand-name">RM Cargoline</span>
    </div>

    <div class="holder">
      <p class="holder-name">Berki Zsófia</p>
      <p class="holder-title">General Manager</p>
    </div>

    <ul class="contact-list">
      <li class="contact-item">
        <span>+36-70/482-5193</span>
        <svg class="contact-icon" viewBox="0 0 16 16" aria-label="Mobile"><path d="M4 1.5 L6.5 1 L7.5 4.5 L5.8 5.6 C6.5 7.6 8 9.4 10 10.3 L11.2 8.7 L14.5 9.8 L14 12.5 C9 13 3.5 7 4 1.5 Z" fill="none" stroke="var(--brand-blue)" stroke-width="1.3"/></svg>
      </li>
      <li class="contact-item">
        <span>+36-1/534-9061</span>
        <svg class="contact-icon" viewBox="0 0 16 16" aria-label="Fax"><rect x="4" y="1.5" width="8" height="4" fill="var(--brand-blue)"/><rect x="1" y="6" width="14" height="6" rx="1" fill="var(--brand-blue)"/><rect x="4" y="10" width="8" height="4.5" fill="var(--brand-blue)" stroke="var(--card-dark)" stroke-width="1"/></svg>
      </li>
      <li class="contact-item">
        <span>zsofia.berki@rmcargoline.example</span>
        <svg class="contact-icon" viewBox="0 0 16 16" aria-label="Email"><rect x="1" y="3" width="14" height="10" fill="var(--brand-blue)"/><path d="M1 3.5 L8 9 L15 3.5 M1 12.5 L6 8 M15 12.5 L10 8" stroke="var(--card-dark)" stroke-width="1.1" fill="none"/></svg>
      </li>
      <li class="contact-item">
        <span>www.rmcargoline.example</span>
        <svg class="contact-icon" viewBox="0 0 16 16" aria-label="Website"><g fill="none" stroke="var(--brand-blue)" stroke-width="1.1"><circle cx="8" cy="8" r="6.5"/><ellipse cx="8" cy="8" rx="3" ry="6.5"/><path d="M1.5 8 H14.5 M2.5 4.8 H13.5 M2.5 11.2 H13.5"/></g></svg>
      </li>
      <li class="contact-item">
        <span>info@rmcargoline.example</span>
        <svg class="contact-icon" viewBox="0 0 16 16" aria-label="Information"><circle cx="8" cy="8" r="6.8" fill="none" stroke="var(--brand-blue)" stroke-width="1.1"/><circle cx="8" cy="4.8" r="0.9" fill="var(--brand-blue)"/><path d="M8 7 V12" stroke="var(--brand-blue)" stroke-width="1.4"/></svg>
      </li>
    </ul>
  </section>

</div>
</body>
</html>
```